Winter Carnival - FUN Web Design Project

The winter carnival is celebrating it's 50th anniversary this year and we are looking to have a new website that will not only work for the 50th, but will work for future years as well (so cannot be 100% geared to the anniversary in terms of look & feel).

The primary focus of the Carnival is the events that take place through the 10-day carnival, and giving recognition to the sponsors (rotating logos on splash page / interior).

The primary colours of the Carnival are Red and White. For some background information - see the old site parked here: http://www.plavetro.on.ca/content.php?ID=34

For the design concepts, we welcome stock photography as we would like to see several photos located prominently throughout the site which we will provide once the site is being constructed (no need to buy stock - we have lots of photos that we can use once a design is selected).

The carnival is a WINTER carnival - so obviously a winter theme utilizing the Red / White colours of our brand.

PSD files will be required so we can code the site to our needs from a technical perspective.
Updates

Good quality GIF of logo attached with lower-quality (sorry) version of the Wordmark uploaded to Project File.

Date extended 1 day to Sunday!

Industry/Entity Type

Events

Requirements
Must have
• Prominent placement for key sponsor logos
Links to social media - PageRing / Chirplo / Boardlyn
Photo-friendly website
Incorporation of corporate colours - Red / White
1 x Home/Splash page layout - emphasis on sponsors, photos, featured event
1 x Interior page layout - more focused on content - see http://www.plavetro.on.ca/content.php?ID=34
Site search bar
Drop-down navigation / changing colour rollovers
Child - Friendly

Nice to have
• Banner/Image links to other site features:
- news
- photo gallery
- History

```html
<!DOCTYPE html>
<html lang="en">
<head>
<meta charset="utf-8">
<title>Norland's Winter Carnival Plavetro</title>
<link rel="stylesheet" href="https://fonts.googleapis.com/css2?family=Arimo:wght@400;700&display=swap">
<style>
:root{
  --red:#d3151d;
  --red-dark:#b50f16;
  --blue:#4a86d6;
  --blue-light:#7fb0ea;
  --text:#3d3d3d;
  --muted:#6a6a6a;
  --grey-bar:#f0f0f0;
  --line:#cfcfcf;
  --white:#ffffff;
}
*{margin:0;padding:0;box-sizing:border-box}
html,body{width:1190px;height:1200px;overflow:hidden}
body{
  position:relative;
  font-family:"Arimo",Arial,sans-serif;
  color:var(--text);
  background:linear-gradient(90deg,#8cc0ec 0%,#cfe3f5 9%,#eef5fb 13%,#ffffff 16%,#ffffff 84%,#eef5fb 88%,#e4eef8 100%);
}
.abs{position:absolute}
.page{position:absolute;left:159px;top:0;width:873px;height:1200px;background:var(--white)}
.mascot{left:213px;top:102px;width:69px;height:86px;border-radius:30px 30px 12px 12px;background:linear-gradient(180deg,#f4f4f4 0%,#f4f4f4 45%,var(--red) 46%,var(--red) 100%)}
.bubble{left:298px;top:49px;width:138px;height:83px;border:1px solid #dcdcdc;border-radius:8px;background:#fff;padding:14px 8px 0 11px;font-size:10.5px;line-height:17px;color:#555}
.bubble-hat{left:418px;top:38px;width:32px;height:26px;border-radius:4px 16px 4px 4px;background:linear-gradient(135deg,#e5262b,#b80f15)}
.thanks{left:781px;top:97px;font-size:11px;color:#333}
.circle-btn{width:26px;height:26px;border-radius:50%;background:#fff;border:1px solid #dadada;box-shadow:0 1px 3px rgba(0,0,0,.15);display:flex;align-items:center;justify-content:center}
.sponsor-name{left:822px;top:140px;font-size:24px;color:#222}
.nav{left:145px;top:190px;width:887px;height:36px;background:linear-gradient(180deg,#e2242b,var(--red-dark));}
.nav a{position:absolute;top:9px;font-size:14px;color:#fff;text-decoration:none}
.nav-pointer{left:407px;top:220px;width:0;height:0;border-left:6px solid transparent;border-right:6px solid transparent;border-bottom:6px solid var(--grey-bar)}
.search{left:825px;top:195px;width:156px;height:26px;background:#fff;border-radius:13px;font-size:11px;color:#666;padding:6px 0 0 12px}
.search-btn{left:956px;top:195px;width:26px;height:26px;border-radius:50%;background:var(--red);display:flex;align-items:center;justify-content:center}
.crumbs{left:159px;top:226px;width:873px;height:31px;background:var(--grey-bar)}
.crumb-text{left:206px;top:235px;font-size:10.5px;color:#555}
.follow{left:837px;top:235px;font-size:10.5px;color:#555}
.social{top:233px;width:14px;height:14px;border-radius:2px}
.bar-blue{left:206px;top:284px;width:777px;height:36px;border-radius:8px;background:linear-gradient(180deg,var(--blue-light),var(--blue))}
.bar-blue span{position:absolute;top:10px;font-size:15.5px;color:#fff}
.news-title{left:226px;top:327px;font-size:16px;color:var(--red)}
.news-date{left:229px;top:347px;font-size:9px;color:#555}
.photo{border-radius:8px}
.body-text{font-size:11.5px;line-height:18.8px;color:var(--text)}
.news-body{left:228px;top:478px;width:350px}
.news-body p+p{margin-top:18.8px}
.photos-body{left:619px;top:476px;width:340px}
.photos-body .zoom{color:var(--red)}
.other-title{left:631px;top:545px;font-size:16px;color:var(--blue)}
.other-list{left:633px;top:571px;list-style:none;font-size:11.5px;color:var(--text)}
.other-list li{height:22.5px;display:flex;align-items:center;gap:8px}
.bar-light{left:206px;top:700px;width:777px;height:37px;border-radius:8px;background:linear-gradient(180deg,#ffffff,#f1f1f1);box-shadow:0 1px 3px rgba(0,0,0,.12)}
.bar-light span{position:absolute;left:20px;top:10px;font-size:15.5px;color:var(--blue)}
.gallery{left:206px;top:746px;width:774px;height:231px;border-radius:8px;background:linear-gradient(90deg,#c9dcea 0%,#e6eff5 40%,#f2f2ef 60%,#d6e6ef 100%)}
.gallery-cta{left:249px;top:779px;width:174px;height:174px;border-radius:50%;background:rgba(40,46,52,.88);color:#fff;font-size:19.5px;line-height:28px;padding:55px 0 0 29px}
.footer-rule{left:206px;top:1023px;width:773px;height:1px;background:var(--line)}
.copyright{left:206px;top:1034px;font-size:11.5px;color:#333}
.copyright b{font-weight:400;color:var(--red)}
.footer-links{right:211px;top:1034px;font-size:11.5px;color:#333;display:flex;gap:10px}
.partner-name{left:210px;top:1100px;font-size:24px;color:#8a8a8a}
.badge{border-radius:4px}
</style>
</head>
<body>
<div class="page"></div>

<header>
  <div class="abs mascot" role="img" aria-label="Carnival snowman mascot in red hat and shirt"></div>
  <div class="abs bubble">Welcome to Norland's Winter Carnival Plavetro. See our gallery! :)</div>
  <div class="abs bubble-hat" role="img" aria-label="Small red winter hat on the speech bubble"></div>

  <div class="abs thanks">We say ‘thank you’ to all our sponsors:</div>
  <div class="abs circle-btn" style="left:778px;top:141px">
    <svg width="8" height="10" viewBox="0 0 8 10"><path d="M6 1 2 5l4 4" fill="none" stroke="#555" stroke-width="1.6"/></svg>
  </div>
  <div class="abs sponsor-name">Norland</div>
  <div class="abs circle-btn" style="left:955px;top:141px">
    <svg width="8" height="10" viewBox="0 0 8 10"><path d="M2 1l4 4-4 4" fill="none" stroke="#555" stroke-width="1.6"/></svg>
  </div>

  <nav class="abs nav">
    <svg class="abs" style="left:66px;top:12px" width="12" height="11" viewBox="0 0 12 11"><path d="M6 0 0 5.5h1.8V11h3V7.5h2.4V11h3V5.5H12z" fill="#fff"/></svg>
    <a style="left:97px">Home</a>
    <a style="left:162px">Events</a>
    <a style="left:231px">Photo Gallery</a>
    <a style="left:338px">Sponsors</a>
    <a style="left:423px">Carnival Info</a>
    <a style="left:525px">Contact us</a>
  </nav>
  <div class="abs search">Search your phrase...</div>
  <div class="abs search-btn">
    <svg width="11" height="11" viewBox="0 0 11 11"><circle cx="4.5" cy="4.5" r="3.2" fill="none" stroke="#fff" stroke-width="1.6"/><path d="M7 7l3 3" stroke="#fff" stroke-width="1.8"/></svg>
  </div>
</header>

<div class="abs crumbs"></div>
<div class="abs nav-pointer"></div>
<div class="abs crumb-text">You are here: Home</div>
<div class="abs follow">Follow us on:</div>
<div class="abs social" style="left:907px;background:#3b5a9a" role="img" aria-label="PageRing"></div>
<div class="abs social" style="left:927px;background:#4fb3e6" role="img" aria-label="Chirplo"></div>
<div class="abs social" style="left:947px;background:#c8202b" role="img" aria-label="Boardlyn"></div>
<div class="abs social" style="left:966px;background:#d8262a" role="img" aria-label="Video channel"></div>

<main>
  <div class="abs bar-blue"><span style="left:20px">Latest news</span><span style="left:410px">Latest photos</span></div>

  <h2 class="abs news-title" style="font-weight:400">Thank You, Volunteers!</h2>
  <div class="abs news-date">DATE: 11.12.2012.</div>
  <div class="abs photo" style="left:226px;top:365px;width:340px;height:107px;background:linear-gradient(90deg,#2f5fb8 0%,#9fc3e2 30%,#f0f0ee 55%,#cfe3ee 100%)" role="img" aria-label="Snowman mascot beside an ice palace"></div>
  <div class="abs body-text news-body">
    <p>Plavetro is delighted to recognize Volunteer Week 2013! We are powered by Volunteers; starting with the 11 dedicated Directors on our own Board, right through to the 509 wonderful people who helped with Plavetro 2012, and we thank you all!</p>
    <p>"Our" Volunteers are also Volunteers with so many other great Agencies and Events - the Volunteer Spirit of this City is truly one of the things that makes us Naturally Bright.As we prepare for Plavetro's 50th Anniversary, and "Shine On!" in Frost Harbour, we take this special week to say, from the bottom of our hearts,</p>
  </div>

  <div class="abs photo" style="left:616px;top:330px;width:340px;height:142px;background:linear-gradient(180deg,#a9c6e2 0%,#5d7a52 35%,#dfe6ee 70%,#f3f5f8 100%)" role="img" aria-label="Mascot greeting families at the winter carnival"></div>
  <div class="abs circle-btn" style="left:598px;top:386px;width:38px;height:38px">
    <svg width="8" height="10" viewBox="0 0 8 10"><path d="M6 1 2 5l4 4" fill="none" stroke="#333" stroke-width="1.8"/></svg>
  </div>
  <div class="abs circle-btn" style="left:938px;top:386px;width:38px;height:38px">
    <svg width="8" height="10" viewBox="0 0 8 10"><path d="M2 1l4 4-4 4" fill="none" stroke="#333" stroke-width="1.8"/></svg>
  </div>
  <div class="abs body-text photos-body">It is a long established fact that a reader will be distracted by the readable content of a page when looking at its layout.<br><span class="zoom">Click on the picture to zoom.</span></div>

  <svg class="abs" style="left:619px;top:552px" width="5" height="8" viewBox="0 0 5 8"><path d="M5 0 0 4l5 4z" fill="var(--blue)"/></svg>
  <div class="abs other-title">Other news:</div>
  <ul class="abs other-list">
    <li><svg width="10" height="8" viewBox="0 0 10 8"><path d="M1 4l3 3 5-6" fill="none" stroke="#555" stroke-width="1.8"/></svg>Happy Victoria Day, 12.04.2012</li>
    <li><svg width="10" height="8" viewBox="0 0 10 8"><path d="M1 4l3 3 5-6" fill="none" stroke="#555" stroke-width="1.8"/></svg>Northgate Winners, 15.09.2013</li>
    <li><svg width="10" height="8" viewBox="0 0 10 8"><path d="M1 4l3 3 5-6" fill="none" stroke="#555" stroke-width="1.8"/></svg>Our new sponsor - Grill Crown, 12.01.2013</li>
    <li><svg width="10" height="8" viewBox="0 0 10 8"><path d="M1 4l3 3 5-6" fill="none" stroke="#555" stroke-width="1.8"/></svg>Volunteer's week, 07.05.2011</li>
  </ul>

  <div class="abs bar-light"><span>Photo gallery</span></div>
  <div class="abs gallery" role="img" aria-label="Snowman mascot in red hat in front of an ice palace"></div>
  <div class="abs gallery-cta">Click here to<br>see our gallery</div>
</main>

<footer>
  <div class="abs footer-rule"></div>
  <div class="abs copyright">Copyright by <b>Norland's Winter Carnival 2012</b>. All rights reserved.</div>
  <div class="abs footer-links"><span>Home</span><span>Events</span><span>Gallery</span><span>Sponsors</span><span>Carnival Info</span><span>Contact</span></div>

  <div class="abs partner-name">Norland</div>
  <div class="abs badge" style="left:390px;top:1083px;width:76px;height:70px;background:#e4e4e4" role="img" aria-label="Partner badge"></div>
  <div class="abs badge" style="left:532px;top:1083px;width:139px;height:63px;background:#ececec" role="img" aria-label="Partner badge"></div>
  <div class="abs badge" style="left:735px;top:1082px;width:86px;height:60px;background:#8fc43c" role="img" aria-label="Partner badge"></div>
  <div class="abs badge" style="left:877px;top:1083px;width:107px;height:64px;background:#ececec" role="img" aria-label="Partner badge"></div>
</footer>
</body>
</html>
```